Business Card Design for drone videography and photography

I have a Vexor Talon 3 drone. I am looking for a logo to somehow incorporate with my business name. I don't even know what is an appropriate font. I am most filming real estate homes. I want something simplistic and a logo that makes sense for the business that I'm in. xxxxxxxxxxxxxxxxxxxxxxxxxxxxxxxxxxxxxxxxxxxxxxxxxxxxxxxxxxxxxxxxxxxxxxxxxxxxxxxxxxxxxxxxxxxxxxxxxxxxxxxxxxxxxxxxxxxxxxxxxxxxxxxxxxxxxxxxxxxxxxxxxxxxxxxxxxxxxxxxxxxxxxxxxxxxxxxxxxxxxxxxxxxxxxxxxxxxxxxxxxxxxxxxxxxxxxxxxxxxxxxxxxxxxxxxxxxxxxxxxxxxxxxxxxxxxxxxxxxxxxxxxxxxxxxxxxxxxxxxxxxxxxxxxxxxxxxxxxxxxxxxxxxxxxxxxxxxxxxxxxxxxxxxxxxxxxxxxxxxxxxxxxxxxxxxxxxxxxxxxxxxxxxxxxxxxxxxxxxxxxxxxxxxxxxxxxxxxxxxxxxxxxxxxxxxxxxxxxxxxxxxxxxxxxxxxxxxxxxxxxxxxxxxxxxxxxxxxxxxxxxxxxxxxxxxxxxxxxxxxxxxxxxxxxxxxxxxxxxxxxxxxxxxxxxxxxxxxxxxxxxxxxxxxxxxxxxxxxxxxxxxxxxxxxxxxxxxxxxxxxxxxxxxxxxxxxxxxxxxxxxxxxxxxxxxxxxxxxxxxxxxxxxxxxxxxxxxxxxxxxxxxxxxxxxxxxxxxxxxxxxxxxxxxxxxxxxxxxxxxxxxxxxxxxxxxxxxxxxxxxxxxxxxxxxxxxxxxxxxxxxxxxxxxxxxxxxxxxxxxxxxxxxxxxxxxxxxxxxxxxxxxxxxxxxxxxxxxxxxxxxxxxxxxxxxxxxxxxxxxxxxxxxxxxxxxxxxxxxxxxxxxxxxxxxxxxxxxxxxxxxxxxxxxxxxxxxxxxxxxxxxxxxxxxxxxxxxxxxxxxxxxxxxxxxxxxxxxxxxxxxxxxxxxxxxxxxxxxxxxxxxxxxxxxxxxxxxxxxxxxxxxxxxxxxxxxxxxxxxxxxxxxxxxxxxxxxxxxxxxxxxxxxxxxxxxxxxxxxxxxxxxxxxxxxxxxxxxxxxxxxxxxxxxxxxxxxxxxxxxxxxxxxxxxxxxxxxxxxx

Target Market(s)

Real estate

Industry/Entity Type

Business

Contact Information for Business Card

BRANDT SKYVIEW STUDIO
Daniel Brandt
Owner/Operator

48305 Birch Way
Alder Falls KS 66021

314-720-4163
dbrandt@brandtskyviewstudio.example

NCQ Drone Certified
Insured
Section 333 Exempt
Halvo Wing Class Certified

Font styles to use
Other font styles liked:
• PUMP DEMI BOLD LET

Requirements
Must have
• Maybe have the certifications on the back??? The business card must be more serious than playful
Nice to have
• Possibly have the logo work itself into the business name?
Should not have
• nothing that looks like a "fun" business. I want this business card to look professional but also simplistic. I don't want a picture that I took from my drone as the background.

```html
<!DOCTYPE html>
<html lang="en">
<head>
<meta charset="utf-8">
<title>Brandt Skyview Studio – Business Card</title>
<link href="https://fonts.googleapis.com/css2?family=Questrial&display=swap" rel="stylesheet">
<style>
  :root {
    --backdrop: #d9d9d9;
    --card-light: #f4f4f2;
    --card-dark: #2b2b2b;
    --ink-dark: #2a2a2a;
    --ink-mid: #4a4a4a;
    --ink-light: #d6d6d6;
    --ink-soft: #a9a9a9;
  }
  * { box-sizing: border-box; margin: 0; padding: 0; }
  html, body {
    width: 1200px; height: 747px; overflow: hidden;
    background: var(--backdrop);
    font-family: "Questrial", sans-serif;
  }
  .stage {
    width: 1200px; height: 747px;
    display: flex; align-items: center; justify-content: center; gap: 40px;
  }
  .card {
    width: 540px; height: 309px; position: relative; overflow: hidden;
    box-shadow: 0 2px 6px rgba(0,0,0,0.18);
  }
  .card--front { background: var(--card-light); color: var(--ink-dark); }
  .card--back { background: var(--card-dark); color: var(--ink-light); }

  .brand { display: flex; align-items: center; white-space: nowrap; }
  .brand-name { font-weight: 400; text-transform: uppercase; line-height: 1.2; }
  .brand-dot {
    flex: none; border-radius: 50%; background: currentColor;
  }

  .card--front .brand { position: absolute; left: 34px; bottom: 44px; gap: 10px; }
  .card--front .brand-dot { width: 12px; height: 12px; }
  .card--front .brand-name { font-size: 14px; letter-spacing: 2.5px; color: var(--ink-dark); }

  .contact { position: absolute; left: 268px; top: 38px; right: 20px; }
  .contact__name { font-size: 26px; font-weight: 400; color: var(--ink-dark); line-height: 1.2; }
  .contact__title { font-size: 13px; color: var(--ink-mid); margin-top: 4px; }
  .contact__list { list-style: none; margin-top: 18px; }
  .contact__item {
    display: flex; align-items: flex-start; gap: 10px;
    font-size: 13px; line-height: 1.45; color: var(--ink-mid);
    margin-bottom: 10px;
  }
  .contact__icon { flex: none; width: 13px; height: 13px; margin-top: 3px; fill: var(--ink-dark); }
  .contact__email { font-size: 12px; white-space: nowrap; }

  .card--back .brand { position: absolute; left: 40px; top: 50px; gap: 14px; }
  .card--back .brand-dot { width: 14px; height: 14px; }
  .card--back .brand-name { font-size: 22px; letter-spacing: 3px; color: var(--ink-light); }

  .credentials {
    position: absolute; left: 40px; bottom: 34px;
    display: flex; align-items: center; gap: 22px;
  }
  .credentials__seal {
    flex: none; width: 66px; height: 66px; border-radius: 50%;
    background: var(--ink-soft);
  }
  .credentials__list { list-style: none; }
  .credentials__item { font-size: 14px; line-height: 1.6; color: var(--ink-light); }
</style>
</head>
<body>
<main class="stage">
  <section class="card card--front" aria-label="Card front">
    <div class="brand">
      <span class="brand-dot" aria-hidden="true"></span>
      <span class="brand-name">Brandt Skyview Studio</span>
    </div>
    <div class="contact">
      <h1 class="contact__name">Daniel Brandt</h1>
      <p class="contact__title">Owner/Operator</p>
      <ul class="contact__list">
        <li class="contact__item">
          <svg class="contact__icon" viewBox="0 0 12 12" aria-hidden="true"><path d="M6 0a4 4 0 0 0-4 4c0 3 4 8 4 8s4-5 4-8a4 4 0 0 0-4-4zm0 5.6A1.6 1.6 0 1 1 6 2.4a1.6 1.6 0 0 1 0 3.2z"/></svg>
          <span>48305 Birch Way<br>Alder Falls KS 66021</span>
        </li>
        <li class="contact__item">
          <svg class="contact__icon" viewBox="0 0 12 12" aria-hidden="true"><path d="M1 3c0-1 1-1.6 2-1.6h6c1 0 2 .6 2 1.6v.8H8.5v-.7h-5v.7H1zM1.5 5h9l.5 5.5H1zM6 6.2a1.6 1.6 0 1 0 0 3.2 1.6 1.6 0 0 0 0-3.2z"/></svg>
          <span>314-720-4163</span>
        </li>
        <li class="contact__item">
          <svg class="contact__icon" viewBox="0 0 12 12" aria-hidden="true"><path d="M0 2.5h12v7H0zm1 .8L6 7l5-3.7v-.1H1z"/></svg>
          <span class="contact__email">dbrandt@brandtskyviewstudio.example</span>
        </li>
      </ul>
    </div>
  </section>

  <section class="card card--back" aria-label="Card back">
    <div class="brand">
      <span class="brand-dot" aria-hidden="true"></span>
      <span class="brand-name">Brandt Skyview Studio</span>
    </div>
    <div class="credentials">
      <div class="credentials__seal" aria-hidden="true"></div>
      <ul class="credentials__list">
        <li class="credentials__item">NCQ Drone Certified</li>
        <li class="credentials__item">Insured</li>
        <li class="credentials__item">Section 333 Exempt</li>
        <li class="credentials__item">Halvo Wing Class Certified</li>
      </ul>
    </div>
  </section>
</main>
</body>
</html>
```